uLark

We need ideas for powerpoint template. Please submit several designs from simple/basic to elaborate/detailed using our company's logo. Please match designs with our logo color. We're very open to ideas. "Harbors Harmonized" can be removed

```html
<!DOCTYPE html>
<html lang="en">
<head>
<meta charset="utf-8">
<title>uLark Presentation Template</title>
<link rel="stylesheet" href="https://fonts.googleapis.com/css2?family=Montserrat:wght@800&family=Poppins:wght@300;400;600&display=swap">
<style>
  :root{
    --board:#d9e2e4;
    --paper:#ffffff;
    --teal-deep:#276f86;
    --teal-mid:#2f8595;
    --teal-soft:#5bb6b0;
    --aqua:#5fe1dc;
    --ink:#1d1d1f;
    --grey:#7a7a7a;
    --rule:#9a9a9a;
    --label:#3a3a3a;
  }
  *{margin:0;padding:0;box-sizing:border-box}
  html,body{width:1152px;height:1200px;overflow:hidden;background:var(--board)}
  .board{position:relative;width:1152px;height:1200px;font-family:"Poppins",sans-serif}
  .page-label{position:absolute;transform:translateX(-50%);font-weight:300;font-size:21px;color:var(--label);letter-spacing:.5px;white-space:nowrap}
  .slide{position:absolute;width:477px;height:269px;background:var(--paper);box-shadow:0 14px 14px -10px rgba(0,0,0,.28)}
  .slide svg{display:block;width:100%;height:100%}
  .title{font-family:"Montserrat",sans-serif;font-weight:800;fill:var(--ink)}
  .sub{font-family:"Poppins",sans-serif;font-size:4px;fill:var(--ink)}
  .head{font-family:"Poppins",sans-serif;font-weight:600;font-size:11px;fill:var(--ink)}
  .body{font-family:"Poppins",sans-serif;font-size:8px;fill:var(--grey)}
  .num{font-family:"Montserrat",sans-serif;font-weight:800;font-size:32px;fill:url(#numGrad)}
  .bar-text{font-family:"Poppins",sans-serif;font-weight:600;font-size:11px;fill:#fff}
  .rule{stroke:var(--rule);stroke-width:1}
  .corner-mark{fill:var(--teal-soft);opacity:.35}
</style>
</head>
<body>
<div class="board">

  <svg width="0" height="0" style="position:absolute">
    <defs>
      <linearGradient id="numGrad" x1="0" y1="0" x2="0" y2="1">
        <stop offset="0" stop-color="#5bb6b0"/><stop offset="1" stop-color="#276f86"/>
      </linearGradient>
      <linearGradient id="photoGrad" x1="0" y1="0" x2="1" y2="1">
        <stop offset="0" stop-color="#cfe3e8"/><stop offset=".5" stop-color="#eef3f4"/><stop offset="1" stop-color="#b9d3db"/>
      </linearGradient>
      <linearGradient id="ringGrad" x1="0" y1="0" x2="0" y2="1">
        <stop offset="0" stop-color="#5fa9b2"/><stop offset="1" stop-color="#2f7f93"/>
      </linearGradient>
      <linearGradient id="heroGrad" x1="0" y1="1" x2="1" y2="0">
        <stop offset="0" stop-color="#246b83"/><stop offset="1" stop-color="#5db4b0"/>
      </linearGradient>
    </defs>
  </svg>

  <div class="page-label" style="left:392px;top:38px">COVER PAGE 1</div>
  <div class="page-label" style="left:892px;top:38px">PAGE1</div>
  <div class="page-label" style="left:392px;top:389px">PAGE 2</div>
  <div class="page-label" style="left:892px;top:389px">PAGE3</div>
  <div class="page-label" style="left:577px;top:1146px">PAGE 4</div>

  <!-- Cover -->
  <div class="slide cover" style="left:74px;top:91px">
    <svg viewBox="0 0 621 350">
      <rect width="621" height="350" fill="url(#photoGrad)" role="img" aria-label="Product photograph of a dropper bottle and white diffuser"/>
      <circle cx="80" cy="175" r="340" fill="url(#ringGrad)"/>
      <circle cx="80" cy="175" r="290" fill="var(--paper)"/>
      <circle cx="177" cy="158" r="49" fill="var(--teal-deep)"/>
      <text x="177" y="233" text-anchor="middle" font-family="Poppins,sans-serif" font-size="22" fill="var(--teal-deep)">uLark</text>
      <text x="177" y="250" text-anchor="middle" font-family="Poppins,sans-serif" font-size="11" fill="var(--teal-deep)">Harbors Harmonized</text>
    </svg>
  </div>

  <!-- Table of content -->
  <div class="slide toc" style="left:598px;top:91px">
    <svg viewBox="0 0 621 350">
      <text class="title" x="306" y="48" text-anchor="middle" font-size="20">TABLE OF CONTENT</text>
      <text class="sub" x="306" y="62" text-anchor="middle">A short subtitle line goes right here</text>
      <g>
        <text class="num" x="60" y="140" text-anchor="middle">1</text>
        <text class="head" x="91" y="115">Lorem Ipsum?</text>
        <text class="body" x="91" y="131">Lorem Ipsum is simply dummy text of the</text>
        <text class="body" x="91" y="142">and typesetting industry.</text>
        <text class="num" x="60" y="202" text-anchor="middle">2</text>
        <text class="head" x="91" y="178">Lorem Ipsum?</text>
        <text class="body" x="91" y="195">Lorem Ipsum is simply dummy text of the</text>
        <text class="body" x="91" y="206">and typesetting industry.</text>
        <text class="num" x="60" y="265" text-anchor="middle">3</text>
        <text class="head" x="91" y="243">Lorem Ipsum?</text>
        <text class="body" x="91" y="260">Lorem Ipsum is simply dummy text of the</text>
        <text class="body" x="91" y="271">and typesetting industry.</text>
      </g>
      <g>
        <text class="num" x="345" y="140" text-anchor="middle">4</text>
        <text class="head" x="376" y="117">Lorem Ipsum?</text>
        <text class="body" x="376" y="134">Lorem Ipsum is simply dummy text of the</text>
        <text class="body" x="376" y="145">and typesetting industry.</text>
        <text class="num" x="345" y="204" text-anchor="middle">5</text>
        <text class="head" x="376" y="176">Lorem Ipsum?</text>
        <text class="body" x="376" y="193">Lorem Ipsum is simply dummy text of the</text>
        <text class="body" x="376" y="204">and typesetting industry.</text>
        <text class="num" x="345" y="267" text-anchor="middle">6</text>
        <text class="head" x="376" y="243">Lorem Ipsum?</text>
        <text class="body" x="376" y="260">Lorem Ipsum is simply dummy text of the</text>
        <text class="body" x="376" y="271">and typesetting industry.</text>
      </g>
      <line class="rule" x1="0" y1="332" x2="560" y2="332"/>
      <circle class="corner-mark" cx="602" cy="334" r="20"/>
    </svg>
  </div>

  <!-- Intro -->
  <div class="slide intro" style="left:72px;top:465px">
    <svg viewBox="0 0 621 350">
      <circle cx="605" cy="175" r="286" fill="url(#heroGrad)" role="img" aria-label="Large brand emblem circle"/>
      <text class="head" x="62" y="148">Lorem Ipsum?</text>
      <text class="body" x="62" y="166">Lorem Ipsum is simply dummy text of the</text>
      <text class="body" x="62" y="177">printing and typesetting industry. Lorem</text>
      <text class="body" x="62" y="188">Ipsum has been the industry's standard</text>
      <text class="body" x="62" y="199">dummy text ever since the 1500s, when</text>
      <text class="body" x="62" y="210">an unknown printer took a galley of a</text>
      <line class="rule" x1="0" y1="332" x2="500" y2="332"/>
    </svg>
  </div>

  <!-- Overview -->
  <div class="slide overview" style="left:594px;top:462px">
    <svg viewBox="0 0 621 350">
      <text class="title" x="295" y="42" text-anchor="middle" font-size="20">PRESENTATION OVERVIEW</text>
      <text class="sub" x="295" y="57" text-anchor="middle">A short subtitle line goes right here</text>
      <g class="rows">
        <g transform="translate(0,92)">
          <text class="head" x="76" y="4">Lorem Ipsum</text>
          <circle cx="190" cy="0" r="8" fill="var(--teal-deep)"/>
          <path d="M212 -5 L220 0 L212 5Z" fill="var(--teal-soft)"/>
          <rect x="235" y="-7.5" width="265" height="15" fill="var(--teal-deep)"/>
          <text class="bar-text" x="242" y="4">Lorem Ipsum</text>
        </g>
        <g transform="translate(0,143)">
          <text class="head" x="76" y="4">Lorem Ipsum</text>
          <circle cx="190" cy="0" r="8" fill="var(--teal-soft)"/>
          <path d="M212 -5 L220 0 L212 5Z" fill="var(--teal-deep)"/>
          <rect x="235" y="-7.5" width="265" height="15" fill="var(--teal-soft)"/>
          <text class="bar-text" x="242" y="4">Lorem Ipsum</text>
        </g>
        <g transform="translate(0,194)">
          <text class="head" x="76" y="4">Lorem Ipsum</text>
          <circle cx="190" cy="0" r="8" fill="var(--teal-deep)"/>
          <path d="M212 -5 L220 0 L212 5Z" fill="var(--teal-soft)"/>
          <rect x="235" y="-7.5" width="265" height="15" fill="var(--teal-deep)"/>
          <text class="bar-text" x="242" y="4">Lorem Ipsum</text>
        </g>
        <g transform="translate(0,244)">
          <text class="head" x="76" y="4">Lorem Ipsum</text>
          <circle cx="190" cy="0" r="8" fill="var(--teal-soft)"/>
          <path d="M212 -5 L220 0 L212 5Z" fill="var(--teal-deep)"/>
          <rect x="235" y="-7.5" width="265" height="15" fill="var(--teal-soft)"/>
          <text class="bar-text" x="242" y="4">Lorem Ipsum</text>
        </g>
        <g transform="translate(0,295)">
          <text class="head" x="76" y="4">Lorem Ipsum</text>
          <circle cx="190" cy="0" r="8" fill="var(--teal-deep)"/>
          <path d="M212 -5 L220 0 L212 5Z" fill="var(--teal-soft)"/>
          <rect x="235" y="-7.5" width="265" height="15" fill="var(--teal-deep)"/>
          <text class="bar-text" x="242" y="4">Lorem Ipsum</text>
        </g>
      </g>
      <line class="rule" x1="0" y1="332" x2="500" y2="332"/>
      <circle class="corner-mark" cx="597" cy="327" r="24"/>
    </svg>
  </div>

  <!-- History -->
  <div class="slide history" style="left:314px;top:839px">
    <svg viewBox="0 0 621 350">
      <text class="title" x="310" y="41" text-anchor="middle" font-size="20">A LITTLE HISTORY</text>
      <text class="sub" x="310" y="56" text-anchor="middle">A short subtitle line goes right here</text>
      <g text-anchor="middle">
        <text class="head" x="96" y="85">Lorem Ipsum?</text>
        <text class="body" x="96" y="105">Lorem Ipsum is simply dummy text of the</text>
        <text class="body" x="96" y="116">and typesetting industry.</text>
        <text class="head" x="319" y="85">Lorem Ipsum?</text>
        <text class="body" x="319" y="105">Lorem Ipsum is simply dummy text of the</text>
        <text class="body" x="319" y="116">and typesetting industry.</text>
        <text class="head" x="529" y="84">Lorem Ipsum?</text>
        <text class="body" x="536" y="104">Lorem Ipsum is simply dummy text of the</text>
        <text class="body" x="538" y="115">and typesetting industry.</text>
      </g>
      <g stroke="var(--ink)" stroke-width="1">
        <line x1="96" y1="137" x2="96" y2="179"/>
        <line x1="313" y1="137" x2="313" y2="179"/>
        <line x1="533" y1="137" x2="533" y2="179"/>
        <line x1="205" y1="216" x2="205" y2="260"/>
        <line x1="424" y1="216" x2="424" y2="260"/>
      </g>
      <g class="timeline">
        <path d="M57 186 H135 L152 207 H40Z" fill="var(--teal-deep)"/>
        <path d="M147 186 H259 L244 207 H162Z" fill="var(--aqua)"/>
        <path d="M275 186 H355 L371 207 H259Z" fill="var(--teal-deep)"/>
        <path d="M367 186 H479 L464 207 H382Z" fill="var(--aqua)"/>
        <path d="M494 186 H573 L589 207 H477Z" fill="var(--teal-deep)"/>
      </g>
      <g text-anchor="middle">
        <text class="head" x="209" y="284">Lorem Ipsum?</text>
        <text class="body" x="219" y="304">Lorem Ipsum is simply dummy text of the</text>
        <text class="body" x="219" y="315">and typesetting industry.</text>
        <text class="head" x="428" y="284">Lorem Ipsum?</text>
        <text class="body" x="438" y="304">Lorem Ipsum is simply dummy text of the</text>
        <text class="body" x="438" y="315">and typesetting industry.</text>
      </g>
      <line class="rule" x1="0" y1="331" x2="500" y2="331"/>
      <circle class="corner-mark" cx="597" cy="326" r="24"/>
    </svg>
  </div>

</div>
</body>
</html>
```